Business Card Design for Retail Product Line

We need a two-sided, full-color business card for a new oral care product line. The feel of the card should invoke emotions of happiness and health. It should be bright, cheerful and modern in appearance. The card should be mostly matte finish, but with elements of spot-gloss and/or raised/embossed features (print, logo, tag lines, etc.).

Target Market(s)

People who are into whole-body health, eat well and understand the importance of nutrition.

Industry/Entity Type

Health And Wellness

Contact Information for Business Card

The logo, color scheme and tag-lines have all been developed and artwork is attached. Card is to be standard-sized and should use a mix of clean, sans-serif fonts; the main font (DIN) is attached as well. The card will be used for 3 individuals and should include placeholders for:
1. Name
2. Title (for example, "CEO")
3. Business address
4. Phone number
5. Website
6. Email address

Font styles to use
Sans Serif
Other font styles liked:
• DIN font

Colors
faa54b
000000
5c5c5c
a2ce44

Requirements
Must have
• 2 sides
• Full color orange on one side
• Image of DNA leaves
• Tag line "Glow from the Root Upward", on single side with orange background
• Company Logo (Plome) on same side as text (name, phone, address, etc.)
• Name, Title, Business Address, Phone Number, Website, Email address
• UPDATE: "Brisk Marrow", not "Brisk M Arrow"
Should not have
• Calligraphy
• Dark colors
• UPDATE!! Do not include "Turmeric infused toothpaste" on the business card
• UPDATE #2!! Do not include "Brisk Marrow" on the business card

```html
<!DOCTYPE html>
<html lang="en">
<head>
<meta charset="utf-8">
<title>Plome business card</title>
<link rel="stylesheet" href="https://fonts.googleapis.com/css2?family=Barlow:wght@700&family=Open+Sans:wght@400;700&display=swap">
<style>
  :root {
    --bg: #efece6;
    --orange-deep: #e9a23c;
    --orange-light: #f3d648;
    --white: #ffffff;
    --green: #8cc63f;
    --green-deep: #4aa032;
    --grey: #5c5c5c;
    --text: #3a3a3a;
  }
  * { box-sizing: border-box; margin: 0; padding: 0; }
  html, body { width: 1200px; height: 970px; overflow: hidden; background: var(--bg); }
  .stage { position: relative; width: 1200px; height: 970px; }

  .card {
    position: absolute; left: 240px; width: 720px; height: 420px;
    border-radius: 18px; overflow: hidden;
    box-shadow: 0 4px 14px rgba(0,0,0,0.18);
  }
  .card--front {
    top: 45px;
    background: linear-gradient(120deg, var(--orange-deep) 0%, #f0c445 55%, var(--orange-light) 75%, #eec040 100%);
  }
  .card--back { top: 505px; background: var(--white); }

  .leaf-decoration {
    position: absolute; left: -60px; top: 20px; width: 440px; height: 460px;
    border-radius: 0 100% 0 100%;
    background: linear-gradient(150deg, rgba(255,255,255,0.22), rgba(255,255,255,0.06));
  }

  .brand {
    position: absolute; right: 60px; top: 78px; text-align: right;
    color: var(--white); font-family: "Barlow", sans-serif; font-weight: 700;
  }
  .brand__name { font-size: 150px; line-height: 1; letter-spacing: -2px; }
  .brand__tagline { margin-top: 18px; font-size: 26px; line-height: 1.05; text-transform: uppercase; }

  .dna-leaves {
    position: absolute; left: 20px; top: 30px; width: 290px; height: 390px;
    border-radius: 60% 40% 0 0;
    background: linear-gradient(160deg, #9fd248 0%, var(--green-deep) 55%, #d2d4d2 100%);
  }

  .identity {
    position: absolute; right: 38px; top: 70px; text-align: right;
    font-family: "Open Sans", sans-serif;
  }
  .identity__name { color: var(--green); font-weight: 700; font-size: 35px; line-height: 1.15; }
  .identity__title { color: var(--grey); font-size: 19px; margin-top: 2px; }

  .brand-mark {
    position: absolute; right: 38px; top: 164px;
    display: flex; align-items: center; gap: 8px;
    font-family: "Open Sans", sans-serif; font-weight: 700;
    font-size: 26px; line-height: 1; color: var(--green);
  }
  .brand-mark__dot { width: 12px; height: 12px; border-radius: 50%; background: var(--green); }

  .contact {
    position: absolute; right: 38px; top: 233px; list-style: none; text-align: right;
    font-family: "Open Sans", sans-serif; font-size: 19px; line-height: 27px; color: var(--text);
  }
  .contact__item { display: flex; justify-content: flex-end; align-items: center; gap: 6px; }
  .contact__icon { width: 15px; height: 15px; flex: none; }
</style>
</head>
<body>
<main class="stage">
  <section class="card card--front" aria-label="Card front">
    <div class="leaf-decoration" role="img" aria-label="Large faint leaf shape"></div>
    <div class="brand">
      <div class="brand__name">Plome</div>
      <div class="brand__tagline">Glow from the<br>Root Upward</div>
    </div>
  </section>

  <section class="card card--back" aria-label="Card back">
    <div class="dna-leaves" role="img" aria-label="Illustration of a DNA helix growing green leaves"></div>
    <div class="identity">
      <h1 class="identity__name">Corinne L. Dathaway</h1>
      <p class="identity__title">Managing Director</p>
    </div>
    <div class="brand-mark">
      <span class="brand-mark__dot"></span>
      <span class="brand-mark__name">Plome</span>
    </div>
    <ul class="contact">
      <li class="contact__item">(555) 014-2290
        <svg class="contact__icon" viewBox="0 0 16 16"><rect width="16" height="16" rx="3" fill="#8cc63f"/><path d="M5 3.5l1.6 2.4-1 1.1a6 6 0 0 0 3.4 3.4l1.1-1 2.4 1.6-.8 1.6C8 12.6 3.4 8 3.4 4.3z" fill="#fff"/></svg>
      </li>
      <li class="contact__item">cdathaway@example.com
        <svg class="contact__icon" viewBox="0 0 16 16"><rect width="16" height="16" rx="3" fill="#8cc63f"/><rect x="3" y="4.5" width="10" height="7" fill="#fff"/><path d="M3 4.5l5 4 5-4" stroke="#8cc63f" stroke-width="1.2" fill="none"/></svg>
      </li>
      <li class="contact__item">www.example.com
        <svg class="contact__icon" viewBox="0 0 16 16"><circle cx="8" cy="8" r="7" fill="#8cc63f"/><g stroke="#fff" stroke-width="1.1" fill="none"><circle cx="8" cy="8" r="4.5"/><ellipse cx="8" cy="8" rx="2" ry="4.5"/><path d="M3.5 8h9"/></g></svg>
      </li>
      <li class="contact__item">418 Alder Bend Road</li>
      <li class="contact__item">Fairhaven, California 90000</li>
    </ul>
  </section>
</main>
</body>
</html>
```